Metal Fabrication Business Cards

We need a business card for our business of Metal Fabrication/Welding. Our company is called "Hadley's Metal Fabrication"

We are a metal fabrication business which takes on "high class" clients- dealing with some of the biggest builders in Australia. Our work is neat, and the type of work we do is 2nd to none for quality. We want to show that on our cards. However, we would love to show a side that is down to earth and a bit more modern and contemporary - we are all young in business so would love to show that side - rather than a boring "very straight looking" card. We always have a clean workshop and take pride in our presentation. We want to come across like we are very rich, but would love to go for a surf as well! A card that basically says we have high class and will charge you a high rate - but the quality will be outstanding.

Front of card: - Simply but sharp!
-Thinking maybe white card - with nice black writing.
-On the right hand side of card a person welding - or holding a welder.
- My business name - Hadley's Metal Fabrication
-Also maybe my name - which is 'Corey" (if it doesn't work, we can put this on the back of card.)
- if needed to look better - we can put keywords on front of card like "metal fabrication, sheet metal, welding etc" but I dont want it to be crowded.

Back of card: - Also make smart but sharp!
Put details such as:
04387 21 914
hadley.fabrication@tinmailbox.com.au
7/32 Keel Street
South Lismore NSW 2480
www.korvinfabrication.com.au
ABN 72 615 803 914

thats just an idea - its now up to you. I don't mind what you come up with - as long as it stands out from the rest and looks sharp, professional but contemporary.

Business

Put details such as:
04387 21 914
7/32 Keel Street
South Lismore NSW 2480
ABN 72 615 803 914

Hadley's Metal Fabrication

```html
<!DOCTYPE html>
<html lang="en">
<head>
<meta charset="utf-8">
<title>Hadley's Metal Fabrication — Business Card</title>
<link rel="stylesheet" href="https://fonts.googleapis.com/css2?family=Arimo:wght@400;700&display=swap">
<style>
  :root {
    --page: #ffffff;
    --ink: #0b0b0b;
    --card-black: #050505;
    --steel-dark: #9a9a9a;
    --steel-mid: #c9c9c9;
    --steel-light: #f2f2f2;
    --brand-grey: #8c8c8c;
    --brand-light: #d8d8d8;
    --steel: linear-gradient(90deg,
      var(--steel-dark) 0%, var(--steel-light) 14%, var(--steel-mid) 30%,
      var(--steel-light) 46%, var(--steel-dark) 62%, var(--steel-light) 80%,
      var(--steel-mid) 100%);
  }
  * { box-sizing: border-box; margin: 0; padding: 0; }
  html, body {
    width: 1183px; height: 1200px; overflow: hidden;
    background: var(--page);
    font-family: "Arimo", Arial, sans-serif;
  }
  .sheet {
    width: 1183px; height: 1200px;
    display: flex; flex-direction: column; align-items: center;
    justify-content: center; gap: 40px;
  }
  .card {
    position: relative; width: 880px; height: 532px;
    background: var(--card-black); overflow: hidden;
    box-shadow: 0 2px 10px rgba(0,0,0,0.18);
  }
  .band { position: absolute; left: 0; width: 100%; background: var(--steel); }

  /* Front */
  .front .band { top: 30%; height: 40%; display: flex; align-items: center; justify-content: center; }
  .brand-name {
    text-align: center; text-transform: uppercase; font-weight: 400;
    line-height: 1.12; letter-spacing: 1px;
  }
  .front .brand-name { color: var(--brand-grey); font-size: 40px; }

  /* Back */
  .back .band-top { top: 0; height: 15%; }
  .back .band-bottom { top: 47%; height: 53%; }
  .back .brand-block {
    position: absolute; top: 15%; height: 32%; width: 100%;
    display: flex; align-items: center; justify-content: center;
  }
  .back .brand-name { color: var(--brand-light); font-size: 28px; }

  .person {
    position: absolute; left: 13%; top: 63%; width: 20%;
    text-align: center; color: var(--ink);
  }
  .person-name { font-size: 36px; font-weight: 700; letter-spacing: 1px; }
  .person-role { font-size: 16px; font-weight: 700; margin-top: 2px; }

  .contacts {
    position: absolute; left: 42%; top: 53%;
    list-style: none; color: var(--ink);
  }
  .contacts li {
    display: flex; align-items: flex-start; gap: 14px;
    font-size: 20px; font-weight: 700; line-height: 1.2; margin-bottom: 18px;
  }
  .contacts svg { flex: 0 0 20px; width: 20px; height: 20px; margin-top: 2px; }
</style>
</head>
<body>
<main class="sheet">

  <section class="card front" aria-label="Card front">
    <div class="band">
      <p class="brand-name">Hadley's Metal<br>Fabrication</p>
    </div>
  </section>

  <section class="card back" aria-label="Card back">
    <div class="band band-top"></div>
    <div class="brand-block">
      <p class="brand-name">Hadley's Metal<br>Fabrication</p>
    </div>
    <div class="band band-bottom"></div>

    <div class="person">
      <p class="person-name">COREY</p>
      <p class="person-role">DIRECTOR</p>
    </div>

    <ul class="contacts">
      <li>
        <svg viewBox="0 0 20 20" aria-hidden="true"><rect x="5" y="1" width="10" height="18" rx="2" fill="var(--ink)"/><rect x="7" y="4" width="6" height="10" fill="var(--steel-light)"/></svg>
        <span>04387 21 914</span>
      </li>
      <li>
        <svg viewBox="0 0 20 20" aria-hidden="true"><rect x="1" y="4" width="18" height="12" fill="var(--ink)"/><path d="M1 4 L10 11 L19 4" stroke="var(--steel-light)" stroke-width="1.5" fill="none"/></svg>
        <span>hadley.fabrication@tinmailbox.com.au</span>
      </li>
      <li>
        <svg viewBox="0 0 20 20" aria-hidden="true"><g fill="none" stroke="#555" stroke-width="1.3"><circle cx="10" cy="10" r="8"/><ellipse cx="10" cy="10" rx="3.5" ry="8"/><line x1="2" y1="10" x2="18" y2="10"/></g></svg>
        <span>www.korvinfabrication.com.au</span>
      </li>
      <li>
        <svg viewBox="0 0 20 20" aria-hidden="true"><path d="M10 2 L19 10 L16 10 L16 18 L12 18 L12 13 L8 13 L8 18 L4 18 L4 10 L1 10 Z" fill="var(--ink)"/></svg>
        <span>7/32 Keel Street Marlow Heads<br>QLD 4571</span>
      </li>
    </ul>
  </section>

</main>
</body>
</html>
```